Title: “The Copper Harbor, Charting The Tides of Memory, A Sailor’s Notebook”

Cover design for ebook and printable book. Looking for this specific designer

```html
<!DOCTYPE html>
<html lang="en">
<head>
<meta charset="utf-8">
<title>The Copper Harbor — Book Cover</title>
<link href="https://fonts.googleapis.com/css2?family=Federo&family=Josefin+Sans:wght@600;700&display=swap" rel="stylesheet">
<style>
  :root {
    --stage: #2e2e2e;
    --paper: #ffffff;
    --slate: #93afb5;
    --slate-light: #a3bcc1;
    --title-red: #d8262e;
    --band: rgba(170, 196, 200, 0.55);
    --art-light: #e9ece3;
    --art-mid: #b9c7c0;
    --art-dark: #7f978f;
    --blossom: #d98a98;
    --trunk: #8a8580;
  }
  html, body {
    margin: 0;
    width: 1200px;
    height: 1200px;
    overflow: hidden;
    background: var(--stage);
  }
  .cover {
    position: absolute;
    left: 243px;
    top: 20px;
    width: 713px;
    height: 1160px;
    background: var(--paper);
    box-sizing: border-box;
    padding: 14px;
  }
  .cover-inner {
    position: relative;
    width: 100%;
    height: 100%;
    background: var(--slate);
    overflow: hidden;
  }
  .crosses {
    position: absolute;
    inset: 0;
    width: 100%;
    height: 100%;
  }
  .crosses path { fill: var(--slate-light); opacity: 0.8; }
  .title {
    position: absolute;
    left: 0;
    right: 0;
    top: 0;
    margin: 0;
    font-family: "Federo", sans-serif;
    font-weight: 400;
    font-variant: small-caps;
    color: var(--title-red);
    -webkit-text-stroke: 7px var(--paper);
    paint-order: stroke fill;
    text-shadow: 3px 4px 5px rgba(0,0,0,0.35);
    text-align: center;
    letter-spacing: 4px;
  }
  .title span {
    position: absolute;
    left: 0;
    right: 0;
    font-size: 128px;
    line-height: 1;
  }
  .title .line-1 { top: 82px; }
  .title .line-2 { top: 177px; }
  .title .line-3 { top: 275px; }
  .artwork {
    position: absolute;
    left: 0;
    right: 0;
    top: 387px;
    height: 670px;
    background:
      radial-gradient(ellipse 46% 40% at 50% 40%, var(--blossom) 0%, rgba(217,138,152,0.55) 55%, rgba(217,138,152,0) 80%),
      linear-gradient(180deg, rgba(138,133,128,0) 55%, rgba(138,133,128,0.45) 100%),
      radial-gradient(ellipse at 50% 50%, var(--art-light) 0%, var(--art-mid) 70%, var(--art-dark) 100%);
  }
  .subtitle-band {
    position: absolute;
    background: var(--band);
    display: flex;
    align-items: center;
    font-family: "Josefin Sans", sans-serif;
    font-weight: 700;
    text-transform: uppercase;
    color: var(--paper);
    font-size: 60px;
    letter-spacing: 5px;
    text-shadow: 3px 4px 4px rgba(0,0,0,0.55);
    white-space: nowrap;
  }
  .band-1 { left: 0; top: 444px; width: 431px; height: 91px; padding-left: 22px; box-sizing: border-box; }
  .band-2 { left: 102px; top: 588px; width: 597px; height: 94px; padding-left: 48px; box-sizing: border-box; }
  .band-3 { left: 0; top: 755px; width: 515px; height: 92px; padding-left: 6px; box-sizing: border-box; }
  .tagline {
    position: absolute;
    left: 231px;
    top: 945px;
    width: 454px;
    height: 42px;
    background: var(--band);
    display: flex;
    align-items: center;
    justify-content: flex-end;
    padding-right: 18px;
    box-sizing: border-box;
    font-family: "Federo", sans-serif;
    font-variant: small-caps;
    font-size: 29px;
    letter-spacing: 4px;
    color: var(--paper);
    text-shadow: 1px 2px 2px rgba(0,0,0,0.4);
  }
</style>
</head>
<body>
  <div class="cover">
    <div class="cover-inner">
      <div class="artwork" role="img" aria-label="Illustration of a blossoming tree with a heart-shaped crown"></div>
      <svg class="crosses" viewBox="0 0 685 1132" aria-hidden="true">
        <path d="M45 26h47v47h47v30h-47v47H45v-47H-2V73h47z" transform="translate(45,0)"/>
        <path d="M528 36h42v42h42v30h-42v42h-42v-42h-42V78h42z"/>
        <path d="M560 295h32v32h32v24h-32v32h-32v-32h-32v-24h32z"/>
        <path d="M27 860h32v32h32v26h-32v32H27v-32h-30v-26h30z" opacity="0.6"/>
        <path d="M590 860h32v32h32v26h-32v32h-32v-32h-30v-26h30z" opacity="0.6"/>
      </svg>
      <h1 class="title">
        <span class="line-1">The</span>
        <span class="line-2">Copper</span>
        <span class="line-3">Harbor</span>
      </h1>
      <div class="subtitle-band band-1">Charting</div>
      <div class="subtitle-band band-2">The Tides</div>
      <div class="subtitle-band band-3">of Memory</div>
      <div class="tagline">A Sailor’s Notebook</div>
    </div>
  </div>
</body>
</html>
```